New Advertising Company Business Card

A two sided business card. One side with logo only and the other side with my information and maybe my logo again. Looking for something unique and creative, but not too busy. Info would include my name(Marcus Fenley), President, phone number, address, email address, and website. LOGO IS THE BLUE AND WHITE ONE.

Target Market(s)

CEO/VP Level Audience

Industry/Entity Type

Business

Contact Information for Business Card

In Description.

```html
<!DOCTYPE html>
<html lang="en">
<head>
<meta charset="UTF-8">
<title>Kestrel Advertising — Business Card</title>
<link href="https://fonts.googleapis.com/css2?family=Montserrat:wght@500;600&family=Work+Sans:wght@300;400&display=swap" rel="stylesheet">
<style>
  :root {
    --backdrop: #e6e1d9;
    --card-face: #f3f0eb;
    --band: #3a3733;
    --brand-blue: #2a7ea6;
    --ink-grey: #45423f;
    --soft-grey: #c9c4bc;
    --sand: #cdb793;
  }
  * { margin: 0; padding: 0; box-sizing: border-box; }
  html, body {
    width: 1200px;
    height: 1047px;
    overflow: hidden;
    background: var(--backdrop);
  }
  .business-card {
    position: absolute;
    left: 100px;
    top: 238px;
    width: 1000px;
    height: 571px;
    border-radius: 18px;
    overflow: hidden;
    background: var(--card-face);
    box-shadow: 0 10px 30px rgba(60, 50, 40, 0.18);
  }
  .brand-lockup {
    position: absolute;
    left: 57px;
    top: 118px;
    display: flex;
    align-items: flex-start;
    gap: 18px;
  }
  .brand-mark {
    width: 26px;
    height: 26px;
    margin-top: 14px;
    background: var(--brand-blue);
    flex: none;
  }
  .brand-name {
    font-family: "Montserrat", sans-serif;
    font-weight: 500;
    color: var(--ink-grey);
    line-height: 1.05;
    font-size: 58px;
    letter-spacing: 3px;
  }
  .brand-name .brand-line-two {
    display: block;
    font-size: 28px;
    letter-spacing: 7.5px;
    margin-top: 8px;
  }
  .info-band {
    position: absolute;
    left: 0;
    top: 260px;
    width: 100%;
    height: 311px;
    background: var(--band);
  }
  .band-accent {
    position: absolute;
    left: 670px;
    top: 262px;
    width: 290px;
    height: 290px;
    border-radius: 50%;
    background: var(--brand-blue);
  }
  .holder-name {
    position: absolute;
    left: 57px;
    top: 283px;
    font-family: "Montserrat", sans-serif;
    font-weight: 600;
    font-size: 36px;
    letter-spacing: 1.5px;
    color: var(--brand-blue);
    text-transform: uppercase;
  }
  .holder-title {
    position: absolute;
    left: 57px;
    top: 330px;
    font-family: "Work Sans", sans-serif;
    font-weight: 300;
    font-size: 23px;
    color: var(--soft-grey);
  }
  .holder-address {
    position: absolute;
    left: 57px;
    top: 376px;
    font-family: "Work Sans", sans-serif;
    font-weight: 300;
    font-size: 23px;
    line-height: 31px;
    color: var(--soft-grey);
  }
  .contact-list {
    position: absolute;
    left: 57px;
    top: 446px;
    list-style: none;
    font-family: "Work Sans", sans-serif;
    font-weight: 300;
    font-size: 23px;
    line-height: 30px;
    color: var(--sand);
  }
  .contact-list li {
    display: flex;
    align-items: center;
    gap: 17px;
  }
  .contact-icon {
    width: 15px;
    height: 15px;
    flex: none;
  }
</style>
</head>
<body>
  <div class="business-card">
    <div class="brand-lockup">
      <div class="brand-name">KESTREL<span class="brand-line-two">ADVERTISING</span></div>
      <div class="brand-mark" aria-hidden="true"></div>
    </div>

    <div class="info-band"></div>
    <div class="band-accent" role="img" aria-label="Brand accent shape"></div>

    <div class="holder-name">Marcus Fenley</div>
    <div class="holder-title">President</div>
    <div class="holder-address">418 Harrow Creek Road<br>Dalton, OR 97412</div>

    <ul class="contact-list">
      <li>
        <svg class="contact-icon" viewBox="0 0 16 16" aria-hidden="true">
          <path d="M3.5 1.5l2.5 2.8-1.4 1.8c.9 2 2.5 3.6 4.5 4.5l1.8-1.4 2.8 2.5-1.6 2.3C7 13.6 2.4 9 1.2 3.1z" fill="var(--brand-blue)"/>
        </svg>
        541 628 0193
      </li>
      <li>
        <svg class="contact-icon" viewBox="0 0 16 16" aria-hidden="true">
          <rect x="1.5" y="3.5" width="13" height="9" fill="none" stroke="var(--brand-blue)" stroke-width="1.4"/>
          <path d="M1.5 3.5L8 9l6.5-5.5" fill="none" stroke="var(--brand-blue)" stroke-width="1.4"/>
        </svg>
        hello@kestreladvertising.com
      </li>
      <li>
        <svg class="contact-icon" viewBox="0 0 16 16" aria-hidden="true">
          <circle cx="8" cy="8" r="6.3" fill="none" stroke="var(--brand-blue)" stroke-width="1.3"/>
          <ellipse cx="8" cy="8" rx="2.7" ry="6.3" fill="none" stroke="var(--brand-blue)" stroke-width="1.1"/>
          <path d="M1.7 8h12.6" stroke="var(--brand-blue)" stroke-width="1.1"/>
        </svg>
        www.kestreladvertising.com
      </li>
    </ul>
  </div>
</body>
</html>
```